Road Construction Company needs business cards

We would like a new business card designed for our business.

We're a road construction company based in Qld, Australia.

Can the business card please have the following information on it.

Name: Brent Malvoy
Position: General Manager
Phone: 0471 592 304
Email: Brent.malvoy@quendix.com.au
Address: 87 Harrowgate Ave, Pindarra, QLD, 4000
Website: www.quendix.com.au

Visually we'd like the card to be professional and simple.

Attached is our logo.

Our website is www.quendix.com.au

Target Market(s)

Men aged 25-60

Contact Information for Business Card

As listed in project description

Font styles to use
Serif

Requirements
Must have
• Large logo on back of card

```html
<!DOCTYPE html>
<html lang="en">
<head>
<meta charset="utf-8">
<title>Quendix Business Card</title>
<link rel="stylesheet" href="https://fonts.googleapis.com/css2?family=Cinzel:wght@600;700&family=Source+Sans+3:wght@600;700;900&display=swap">
<style>
  :root {
    --navy: #0f55a3;
    --sky: #29a3d9;
    --ink: #111111;
    --paper: #ffffff;
    --stage: #9a9ca1;
  }
  * { margin: 0; padding: 0; box-sizing: border-box; }
  html, body { width: 988px; height: 1200px; overflow: hidden; }
  body { background: var(--stage); position: relative; font-family: "Source Sans 3", sans-serif; }

  .card { position: absolute; width: 841px; height: 478px; border-radius: 42px; overflow: hidden; }
  .card--front { left: 53px; top: 94px; background: var(--navy); }
  .card--back { left: 74px; top: 627px; background: var(--paper); }

  .wordmark { font-family: "Source Sans 3", sans-serif; font-weight: 900; line-height: 1; white-space: nowrap; }
  .card--front .wordmark {
    position: absolute; left: 0; right: 0; top: 180px; text-align: center;
    color: var(--paper); font-size: 112px; letter-spacing: 14px; text-indent: 14px;
  }
  .card--back .wordmark {
    position: absolute; left: 50px; top: 200px; width: 340px; text-align: center;
    color: var(--navy); font-size: 60px; letter-spacing: 7px; text-indent: 7px;
  }

  .divider { position: absolute; left: 425px; top: 100px; width: 1px; height: 272px; background: var(--ink); }

  .contact { position: absolute; left: 464px; top: 94px; color: var(--ink); }
  .contact__name { font-family: "Cinzel", serif; font-weight: 700; font-size: 24px; line-height: 1.1; }
  .contact__role { font-family: "Cinzel", serif; font-weight: 600; font-size: 14px; margin-top: 7px; }
  .contact__address { font-weight: 600; font-size: 19px; line-height: 40px; margin-top: 12px; }
  .contact__list { list-style: none; margin-top: 10px; }
  .contact__item { display: flex; align-items: center; font-weight: 600; font-size: 19px; height: 40px; }
  .contact__icon { width: 22px; height: 22px; margin-right: 16px; flex: none; }

  .card__footer-band { position: absolute; left: 0; right: 0; bottom: 0; height: 22px; background: var(--navy); }
</style>
</head>
<body>
  <section class="card card--front">
    <div class="wordmark">QUENDIX</div>
  </section>

  <section class="card card--back">
    <div class="wordmark">QUENDIX</div>
    <div class="divider"></div>

    <div class="contact">
      <h1 class="contact__name">Brent Malvoy</h1>
      <p class="contact__role">GENERAL MANAGER</p>
      <p class="contact__address">87 Harrowgate Ave,<br>Pindarra, QLD, 4000</p>
      <ul class="contact__list">
        <li class="contact__item">
          <svg class="contact__icon" viewBox="0 0 24 24" aria-hidden="true"><path fill="var(--ink)" d="M6.6 10.8a15.1 15.1 0 0 0 6.6 6.6l2.2-2.2a1 1 0 0 1 1-.25 11.4 11.4 0 0 0 3.6.57 1 1 0 0 1 1 1V20a1 1 0 0 1-1 1A17 17 0 0 1 3 4a1 1 0 0 1 1-1h3.5a1 1 0 0 1 1 1c0 1.250.2 2.45.57 3.57a1 1 0 0 1-.25 1z"/><path fill="none" stroke="var(--ink)" stroke-width="1.6" d="M14 6a4 4 0 0 1 4 4M14 2.5A7.5 7.5 0 0 1 21.5 10"/></svg>
          0471 592 304
        </li>
        <li class="contact__item">
          <svg class="contact__icon" viewBox="0 0 24 24" aria-hidden="true"><rect x="2" y="5" width="20" height="14" fill="var(--ink)"/><path d="M2 5l10 8 10-8M2 19l7.5-7M22 19l-7.5-7" fill="none" stroke="var(--paper)" stroke-width="1.5"/></svg>
          Brent.malvoy@quendix.com.au
        </li>
        <li class="contact__item">
          <svg class="contact__icon" viewBox="0 0 24 24" aria-hidden="true"><g fill="none" stroke="var(--ink)" stroke-width="1.8"><circle cx="12" cy="12" r="10"/><ellipse cx="12" cy="12" rx="4.5" ry="10"/><path d="M2 12h20M4 7h16M4 17h16"/></g></svg>
          www.quendix.com.au
        </li>
      </ul>
    </div>

    <div class="card__footer-band"></div>
  </section>
</body>
</html>
```